Web Design

We need a new website for our company. We perform several functions:

1 - IT and Network Support
2 - Computer Consultancy
3 - Cloud Services
4 - Hosted Mailvane & Online Backup
5 - Internet Connections & VOIP

Examples of some of the designs we like can be seen on:
• www.brelvox.com
• www.quintaro.com

I urgently need a new website to be designed to enable me to look more professional. My competitors website is www.tdmq.co.uk

I also want to be able to look much more professional, like www.brelvox.com www.quintaro.com

I have attached how I would like the website to look

Task outline
To design a home page and another internal skeleton page for a website following our requirements specification and wireframe layout/structure

Task description
We are looking for a modern, attractive, clean design for our new website to reflect our businesses professionalism and high quality services that we offer.
• www.brelvox.com
• www.quintaro.com
We would like a design for a home page and one other skeleton subpage for our website. We have provided a wireframe image to assist, showing how we would like the layout/structure of our website to follow which also highlights where we would like specific content/features to go.
We have listed what features the site must have in the requirements section.
The final design should communicate to our users that we are a professional business that offer high quality services and that we are a company they can trust and rely on.

Look and feel
The wireframe we have attached is a representation of how we would like the layout and structure of the website to be designed. We would like to have a corporate theme to our website.

Colours
Open to interpretation by the designer, as long as the colours suit a corporate theme and give off a professional look and feel.

Requirements
The design must have the following:

General
• Home page design (Based on attached wireframe).
• Internal Page design (This needs to be a skeleton page which can be used for implemented the content for all over pages).

• Contact details to be visible on every page, contact number at the header and all other relative details in the footer section.
• Social networking icons within the footer section of the site.
• Avoid the use of unprofessional images for buttons, icons and banners etc.
Features desired
• Drop down navigation bar. Please see the attached image for inspiration for its design/layout.
o We would like a similar drop down menu design to the one on this site: www.tdmq.co.uk.
• Image slider at the header of every page just beneath the navigation bar.
o We would like the Plexa slider to be used for the image slider. Please use this link for an example of it in action: http://www.scriptloomhub.net/demo/plexa-slider/
o The image slider needs to be larger on the home page.
o The image slider can be smaller on the rest of the pages of the site.
• Chirply feed present on every page.
• News/Blog feed present on every page.
• Call back form present on every page.
• Wayfindr Map implementation above footer on every page.

A user friendly, accessible design that is easy to use and easy for the user to understand. Must have a corporate theme to reflect the professionalism of our business. Content flows logically and keep content spaced out so that it does not make the site look cluttered.

Target Market(s)

Small to Mid sized Business, Large Banks and Legal, corporate, business - non-technical users

Industry/Entity Type

Business

Font styles to use
Sans Serif

```html
<!DOCTYPE html>
<html lang="en">
<head>
<meta charset="utf-8">
<title>Corrandale Systems – IT Support</title>
<link rel="stylesheet" href="https://fonts.googleapis.com/css2?family=Arimo:wght@400;700&display=swap">
<style>
:root{
  --header-blue-top:#2a93cf;
  --header-blue-bottom:#1f86c4;
  --nav-grey:rgba(150,150,150,0.78);
  --nav-text:#ffffff;
  --active-red:#dd5a44;
  --dropdown:rgba(236,96,72,0.88);
  --caption:rgba(62,62,62,0.88);
  --accent-orange:#f0a800;
  --page-bg:#ebebeb;
  --heading-blue:#2b7fd6;
  --body-navy:#1c3a6b;
  --label-blue:#2a78bd;
  --rule-dark:#4a4a4a;
  --icon-dark:#222;
}
*{box-sizing:border-box;margin:0;padding:0}
html,body{width:1200px;height:836px;overflow:hidden}
body{position:relative;background:var(--page-bg);font-family:Arimo,Arial,sans-serif}

.site-header{position:absolute;left:0;top:0;width:1200px;height:160px;
  background:linear-gradient(var(--header-blue-top),var(--header-blue-bottom));
  box-shadow:0 3px 6px rgba(0,0,0,.35);z-index:3}
.brand{position:absolute;left:130px;top:52px;color:#fff;font-size:43px;font-weight:400}
.contact-phone{position:absolute;left:794px;top:42px}
.contact-phone svg{display:block}
.get-in-touch{position:absolute;left:879px;top:54px;color:#fff;font-size:15px;font-weight:700;letter-spacing:.5px}
.phone-number{position:absolute;left:880px;top:73px;color:#fff;font-size:28px;font-weight:700;letter-spacing:1px}

.hero{position:absolute;left:0;top:160px;width:1200px;height:535px;
  background:linear-gradient(100deg,#e9d9cc 0%,#f4ece6 22%,#e8e2dc 40%,#f1eeea 60%,#dcd6d0 80%,#ebe8e4 100%)}
.main-nav{position:absolute;left:0;top:160px;width:1200px;height:65px;background:var(--nav-grey);z-index:2}
.nav-list{position:absolute;left:129px;top:0;height:65px;display:flex;align-items:center;list-style:none;
  color:var(--nav-text);font-size:21px;letter-spacing:1px}
.nav-list .sep{margin:0 14px}
.nav-item.active{background:var(--active-red);color:#222;height:51px;margin-top:24px;padding:0 10px;display:flex;align-items:center;align-self:flex-start;margin-top:12px}

.dropdown{position:absolute;left:328px;top:223px;width:587px;height:236px;background:var(--dropdown);z-index:2;
  color:#fff;font-size:22px}
.dropdown ul{position:absolute;top:30px;list-style:none;line-height:34px}
.dropdown .col-left{left:33px}
.dropdown .col-right{left:301px}

.slide-arrow{position:absolute;top:431px;z-index:1}
.slide-arrow.prev{left:27px}
.slide-arrow.next{left:1144px}

.slide-caption{position:absolute;left:635px;top:313px;width:403px;height:308px;background:var(--caption);
  border-radius:3px;color:#fff;z-index:1}
.slide-caption h2{position:absolute;left:37px;top:32px;font-size:41px;font-weight:400;white-space:nowrap}
.slide-caption p{position:absolute;left:37px;top:92px;width:340px;font-size:19px;line-height:23.8px}
.read-more{color:var(--accent-orange);float:right}
.slide-dots{position:absolute;left:138px;top:266px;display:flex;gap:13px}
.slide-dots span{width:15px;height:15px;background:#8a8a8a}
.slide-dots span.current{background:var(--accent-orange)}

.intro{position:absolute;left:144px;top:720px;width:614px}
.section-title{color:var(--heading-blue);font-size:16px;font-weight:700;letter-spacing:.6px;padding:0 0 10px 2px;
  border-bottom:3px solid var(--rule-dark)}
.intro p{margin-top:14px;color:var(--body-navy);font-size:17px;line-height:28px}

.callback{position:absolute;left:787px;top:711px;width:261px;height:140px;background:#f7f7f7;
  border:2px solid #fff;box-shadow:0 0 3px rgba(0,0,0,.2)}
.callback h3{position:absolute;left:13px;top:12px;font-size:15px;color:#2a2a2a;letter-spacing:.8px}
.callback .rule{position:absolute;left:12px;top:36px;width:234px;height:3px;background:var(--accent-orange)}
.field-label{position:absolute;left:10px;font-size:15px;font-weight:700;color:var(--label-blue)}
.field{position:absolute;left:87px;width:162px;height:25px;background:#fff;border:1px solid #9a9a9a;border-radius:2px}
</style>
</head>
<body>
<header class="site-header">
  <div class="brand">Corrandale Systems</div>
  <div class="contact-phone">
    <svg width="68" height="68" viewBox="0 0 68 68" aria-hidden="true">
      <circle cx="34" cy="34" r="31" fill="none" stroke="#1b1b1b" stroke-width="4"/>
      <path d="M22 17c3-2 6-2 7 1l3 8c1 2 0 4-2 5l-2 2c2 5 5 9 10 12l2-2c1-2 3-2 5-1l7 4c3 2 2 5 0 7l-3 3c-3 2-8 1-13-3-7-5-13-13-16-21-2-6-1-11 2-15z" fill="#1b1b1b"/>
    </svg>
  </div>
  <div class="get-in-touch">GET IN TOUCH</div>
  <div class="phone-number">0141 555 0187</div>
</header>

<div class="hero" role="img" aria-label="Photo of smiling office colleagues at a desk with a laptop"></div>

<nav class="main-nav">
  <ul class="nav-list">
    <li class="nav-item home">
      <svg width="38" height="34" viewBox="0 0 38 34" aria-label="Home">
        <path d="M19 2 2 17h5v15h9v-9h6v9h9V17h5L19 2z" fill="var(--icon-dark)"/>
      </svg>
    </li>
    <li class="sep">|</li><li class="nav-item">COMPANY</li>
    <li class="sep">|</li><li class="nav-item active">IT SUPPORT</li>
    <li class="sep">|</li><li class="nav-item">CLOUD SERVICES</li>
    <li class="sep">|</li><li class="nav-item">PARTNERS</li>
    <li class="sep">|</li><li class="nav-item">CONTACT US</li>
  </ul>
</nav>

<svg class="slide-arrow prev" width="42" height="48" viewBox="0 0 42 48" aria-label="Previous slide">
  <path d="M22 2 2 24l20 22h16L18 24 38 2z" fill="#3a3a3a"/>
</svg>
<svg class="slide-arrow next" width="42" height="48" viewBox="0 0 42 48" aria-label="Next slide">
  <path d="M20 2 40 24 20 46H4l20-22L4 2z" fill="#3a3a3a"/>
</svg>

<div class="slide-caption">
  <h2>Online IT Support</h2>
  <p>This is Pixelcraft's version of Lorem Ipsum. Proin gravida nibh vel velit auctor aliquet. Aenean sollicitu-din, lorem quis bibendum auctor, nisi elit consequat ipsum, nec sagittis sem nibh id elit. <span class="read-more">Read More</span></p>
  <div class="slide-dots"><span></span><span class="current"></span><span></span><span></span><span></span></div>
</div>

<div class="dropdown">
  <ul class="col-left">
    <li>Services</li><li>Business Solutions</li><li>Backup &amp; Recovery</li><li>Broadband</li><li>Consultancy Planning</li>
  </ul>
  <ul class="col-right">
    <li>Email</li><li>Free Audit</li><li>Implementation Services</li><li>Mobile Office</li><li>Network Design</li>
  </ul>
</div>

<section class="intro">
  <h2 class="section-title">CLOUD SERVICES</h2>
  <p>Corrandale Systems Limited is a full-fledged private company that is involved in the provision of business IT solutions to small and</p>
</section>

<aside class="callback">
  <h3>CONTACT US</h3>
  <div class="rule"></div>
  <span class="field-label" style="top:55px">Name</span><div class="field" style="top:52px"></div>
  <span class="field-label" style="top:90px">Email</span><div class="field" style="top:86px"></div>
  <div class="field" style="top:119px"></div>
</aside>
</body>
</html>
```